Plumbing Products Website

This project is to create a web page for Mr. Clear Brook and Mr. Hot Kettle's product offerings. There are 14 unique products. The main page will showcase all 14 products arranged in a clean, concise format that flows nicely and is easy to read.
Furthermore, I need a unique page for each of the 14 products that the main page can link the products to so visitors can click each of them to "Learn More".
For reference, our websites are MrBrookly.example and TopBoilerHub.example; so keep the branding, color-scheme, header, footer, etc. consistent with MrBrookly.example and TopBoilerHub.example.
For reference, here is the catalog. Feel free to copy as much of the content as necessary to build the pages:
https://catalogs.pagefolio.example/MrHotKettle/qvtx/
For clarification, the products are:
1. Whole House Water Purification System
2. Whole House Water Ionization System
3. Whole House Water Softener System
4. Water Heater Sediment Pre-Filter
5. Whole-House UV Water Sterilization System
6. The ULTIMATE Whole House Water Treatment System
7. Under-Sink Reverse Osmosis System with UV Sterilizer
8. Smart Water Heater Regulator with Automated Stand-By for Power Savings
9. Whole House Water Pressure Booster
10. Hot Water Heater Tank Volume Booster
11. Leak Detector with Automatic Water Shutoff
12. Whole House UV Air Purification System
13. Leak Detector Alarm with Mobile App
14. Multi-Gas Detector for Carbon Monoxide, Natural Gas, Propane, Methane, Explosive Gasses, Smoke & Fire
Unfortunately, all the content was created by AI, so I don't have any "original" images or other media. I have attached the logos for your reference though. Also, each individual catalog page is attached.
Once the winning design is chosen, I will need the pages coded and hosted on a staging server for me to view in a live environment before I move them to my server.
Let me know if you have any questions.

```html
<!DOCTYPE html>
<html lang="en">
<head>
<meta charset="utf-8">
<title>Mr. Clear Brook &amp; Mr. Hot Kettle — Water &amp; Home Protection</title>
<link rel="stylesheet" href="https://fonts.googleapis.com/css2?family=Oswald:wght@500;600;700&family=Poppins:wght@400;500;600&display=swap">
<style>
:root{
  --navy:#0b1a5c;
  --navy-deep:#071246;
  --royal:#0d3fb0;
  --blue:#1a4fd0;
  --sky:#3d8cff;
  --light-blue:#5aa6ff;
  --ice:#eef4fd;
  --ink:#1c1f2b;
  --muted:#6c7080;
  --orange:#f57c12;
  --white:#ffffff;
  --line:#e3e8f2;
}
*{box-sizing:border-box;margin:0;padding:0}
html,body{width:1200px;height:2716px;overflow:hidden}
body{position:relative;font-family:'Poppins',sans-serif;color:var(--ink);background:var(--white)}
.abs{position:absolute}
.head{font-family:'Oswald',sans-serif;text-transform:uppercase;font-weight:600}

/* top bar */
.topbar{left:0;top:0;width:1200px;height:35px;background:var(--navy-deep);color:var(--white);font-size:10px;font-weight:500}
.topbar .tag{position:absolute;left:131px;top:11px}
.topbar .contact{position:absolute;right:130px;top:6px;display:flex;align-items:center;gap:8px}
.topbar .contact span{display:flex;align-items:center;gap:5px}
.topbar .sep{width:1px;height:12px;background:#8a94c4}
.social{width:22px;height:22px;border-radius:50%;background:var(--royal)}

/* header + hero */
.hero{left:0;top:35px;width:1200px;height:551px;background:linear-gradient(100deg,#f4f8ff 0%,#e7f0fd 45%,#d3e4fb 100%)}
.brand{position:absolute;display:flex;align-items:center;gap:6px;font-weight:600;font-size:14px;color:var(--royal)}
.brand .dot{width:14px;height:14px;border-radius:50%;background:var(--royal)}
.nav{position:absolute;left:454px;top:24px;display:flex;gap:23px;font-size:10px;font-weight:500;color:var(--ink)}
.nav .active{color:var(--blue);border-bottom:1.5px solid var(--blue);padding-bottom:4px}
.btn{position:absolute;background:var(--orange);color:var(--white);font-size:10.5px;font-weight:600;border-radius:3px;display:flex;align-items:center;justify-content:center}
.hero-title{position:absolute;left:130px;top:170px;font-size:42px;line-height:43px;color:var(--navy);font-weight:700;letter-spacing:.2px}
.hero-lead{position:absolute;left:131px;top:273px;font-size:19px;font-weight:600;color:var(--blue)}
.hero-intro{position:absolute;left:132px;top:312px;width:310px;font-size:13px;line-height:19px;color:var(--ink)}
.perks{position:absolute;left:129px;top:392px;width:421px;height:66px;background:var(--white);border-radius:7px;box-shadow:0 6px 18px rgba(20,60,140,.12);display:flex;align-items:center;justify-content:space-around;padding:0 6px}
.perk{display:flex;align-items:center;gap:6px;font-size:9px;line-height:13px;color:#3b3f4d}
.hero-visual{position:absolute;left:560px;top:64px;width:640px;height:487px;background:radial-gradient(ellipse at 55% 45%,#ffffff 0%,#cfe1fb 45%,#4c8ff0 80%,#2062d8 100%);border-radius:260px 0 0 0}

/* why choose */
.why-title{left:0;top:656px;width:1200px;text-align:center;font-size:29px;color:var(--royal);font-weight:600}
.features{left:132px;top:720px;width:936px;display:flex}
.feature{flex:1;text-align:center;border-right:1px solid var(--line);padding:0 6px;height:142px}
.feature:last-child{border-right:none}
.feature svg{display:block;margin:0 auto 22px}
.feature h3{font-family:'Oswald',sans-serif;text-transform:uppercase;font-weight:500;font-size:16px;line-height:22px;color:var(--ink)}
.feature p{margin-top:13px;font-size:9.5px;line-height:14px;color:var(--muted)}

/* promise band */
.band{left:0;top:862px;width:1200px;height:536px}
.band-house{left:0;top:980px;width:495px;height:362px;background:linear-gradient(160deg,#34508f 0%,#1f3a80 55%,#0c2470 100%);border-radius:0 60px 0 0}
.badge{left:435px;top:905px;width:331px;height:96px;background:linear-gradient(180deg,#0a2a7e,#07205f);border:2px solid #2c63d6;border-radius:10px;box-shadow:0 10px 24px rgba(0,0,0,.3)}
.badge-line{position:absolute;left:95px;top:22px;font-family:'Oswald',sans-serif;font-size:16px;color:var(--white);font-weight:500}
.badge-strong{position:absolute;left:95px;top:42px;font-family:'Oswald',sans-serif;font-size:27px;color:var(--light-blue);font-weight:600}
.band-title{left:580px;top:1063px;font-size:31px;line-height:35px;color:var(--white);font-weight:600}
.band-title span{color:var(--light-blue)}
.band-text{left:581px;top:1142px;width:370px;font-size:12.5px;line-height:19px;color:var(--white);font-weight:500}
.checks{left:580px;top:1226px;width:340px;display:grid;grid-template-columns:126px 98px 116px;row-gap:22px}
.check{display:flex;gap:6px;font-size:9.5px;line-height:13px;color:#dce7ff;font-weight:500;text-transform:uppercase}

/* products */
.prod-title{left:132px;top:1452px;font-size:30px;color:var(--royal);font-weight:600;text-transform:none}
.prod-intro{left:132px;top:1504px;width:310px;font-size:13px;line-height:19px}
.cards{left:132px;top:1568px;width:936px;display:grid;grid-template-columns:repeat(7,124px);column-gap:11.6px;row-gap:12px}
.card{height:172px;background:var(--white);border:1px solid var(--line);border-radius:4px;box-shadow:0 4px 14px rgba(20,50,120,.07);position:relative}
.card-photo{position:absolute;left:9px;top:9px;width:104px;height:72px;border-radius:3px;background:radial-gradient(ellipse at 50% 60%,#dbe9fb 0%,#f3f7fd 70%,#ffffff 100%)}
.card-name{position:absolute;left:10px;top:90px;width:104px;font-size:10.5px;line-height:14px;font-weight:500}
.card-link{position:absolute;left:10px;top:146px;font-size:9.5px;color:var(--blue);text-decoration:none;font-weight:500}

/* testimonials */
.reviews{left:0;top:1950px;width:1200px;height:410px;background:var(--ice)}
.reviews-title{position:absolute;left:0;top:60px;width:1200px;text-align:center;font-size:30px;color:var(--royal);font-weight:600;text-transform:none}
.reviews-sub{position:absolute;left:0;top:109px;width:1200px;text-align:center;font-size:13px;line-height:19px}
.quote{position:absolute;top:173px;width:303px;height:168px;background:var(--white);border:1px solid var(--line);border-radius:6px}
.quote-mark{position:absolute;left:25px;top:22px;font-family:'Oswald',sans-serif;font-size:70px;line-height:60px;color:var(--blue);font-weight:700}
.quote p{position:absolute;left:26px;top:73px;width:255px;font-size:9.5px;line-height:15px;color:#4a4e5c}
.quote-author{position:absolute;left:26px;top:137px;font-size:11.5px;display:flex;align-items:center;gap:6px}
.quote-author::before{content:"";width:14px;height:2px;background:var(--blue)}

/* footer */
.footer{left:0;top:2360px;width:1200px;height:356px;background:var(--navy);color:var(--white)}
.footer-about{position:absolute;left:133px;top:181px;width:230px;font-size:10px;line-height:17px;color:#a9b8ef}
.fcol{position:absolute;top:74px;font-size:10px;font-weight:500}
.fcol h5{font-family:'Oswald',sans-serif;font-size:14px;color:var(--light-blue);font-weight:500;text-transform:uppercase;margin-bottom:16px}
.fcol li{list-style:none;height:31.5px}
.fcol .ci{display:flex;gap:10px;line-height:17px;margin-bottom:17px}
.footer-rule{position:absolute;left:132px;top:302px;width:936px;height:1px;background:#213887}
.footer-copy{position:absolute;left:0;top:316px;width:1200px;text-align:center;font-size:8.5px;line-height:17px;color:#7d8fd3}
</style>
</head>
<body>

<div class="abs topbar">
  <div class="tag">Cleaner Water. Safer Home. Better Life.</div>
  <div class="contact">
    <span><svg width="10" height="10" viewBox="0 0 24 24" fill="none" stroke="#fff" stroke-width="2.2"><path d="M5 3h4l2 5-3 2a11 11 0 0 0 6 6l2-3 5 2v4a2 2 0 0 1-2 2A17 17 0 0 1 3 5a2 2 0 0 1 2-2z"/></svg>555-010-2846</span>
    <i class="sep"></i>
    <span><svg width="11" height="11" viewBox="0 0 24 24" fill="none" stroke="#fff" stroke-width="2"><circle cx="12" cy="12" r="9"/><path d="M3 12h18M12 3c3 3 3 15 0 18M12 3c-3 3-3 15 0 18"/></svg>TopBoilerHub.example</span>
    <i class="social"></i><i class="social"></i>
  </div>
</div>

<header class="abs hero">
  <div class="brand" style="left:133px;top:36px">Mr. Clear Brook<i class="dot"></i></div>
  <div class="brand" style="left:133px;top:62px">Mr. Hot Kettle<i class="dot"></i></div>
  <nav class="nav"><span class="active">HOME</span><span>PRODUCTS</span><span>ABOUT US</span><span>INSTALLATION</span><span>REVIEWS</span><span>CONTACT</span></nav>
  <div class="btn" style="left:973px;top:14px;width:96px;height:31px">Get A Quote</div>

  <h1 class="head hero-title">Complete Water &amp; Home<br>Protection Solutions</h1>
  <div class="hero-lead">14 Powerful Products. 1 Trusted Brand.</div>
  <p class="hero-intro">From cleaner water to smarter home protection – Mr. Clear Brook &amp; Mr. Hot Kettle have everything your home needs.</p>
  <div class="perks">
    <div class="perk"><svg width="18" height="20" viewBox="0 0 24 24" fill="#1a4fd0"><path d="M12 2s7 8 7 13a7 7 0 0 1-14 0c0-5 7-13 7-13z"/></svg>Cleaner Water<br>Better Health</div>
    <div class="perk"><svg width="20" height="20" viewBox="0 0 24 24" fill="none" stroke="#1a4fd0" stroke-width="2.2"><path d="M3 11l9-7 9 7v10H3z"/><rect x="10" y="13" width="4" height="5"/></svg>Smart Home<br>Protection</div>
    <div class="perk"><svg width="22" height="20" viewBox="0 0 24 24" fill="#1a4fd0"><circle cx="12" cy="5" r="3"/><path d="M6 14a6 6 0 0 1 12 0v2H6z"/><rect x="2" y="18" width="20" height="3"/></svg>Professional<br>Installation</div>
    <div class="perk"><svg width="20" height="20" viewBox="0 0 24 24" fill="none" stroke="#1a4fd0" stroke-width="2.2"><circle cx="12" cy="10" r="7"/><path d="M8 16l-2 6 6-3 6 3-2-6M9 10l2 2 4-4"/></svg>Satisfaction<br>Guaranteed</div>
  </div>
  <div class="hero-visual" role="img" aria-label="Cutaway house with water filters, softeners, heaters and detectors in front, surrounded by water splash"></div>
</header>

<h2 class="abs head why-title">Why Choose Mr. Clear Brook &amp; Mr. Hot Kettle?</h2>
<div class="abs features">
  <div class="feature">
    <svg width="54" height="50" viewBox="0 0 48 48" fill="none" stroke="#1a4fd0" stroke-width="3"><circle cx="24" cy="24" r="14"/><path d="M24 16v9l6 4M24 4v5M24 39v5M4 24h5M39 24h5M10 10l4 4M34 34l4 4M10 38l4-4M34 14l4-4"/></svg>
    <h3>Fast &amp; Professional<br>Installation</h3><p>Expert installation done<br>right the first time.</p>
  </div>
  <div class="feature">
    <svg width="50" height="50" viewBox="0 0 48 48" fill="none" stroke="#1a4fd0" stroke-width="3"><circle cx="24" cy="24" r="20" fill="#1a4fd0"/><path d="M14 20l5-6h10l5 6-10 13z" stroke="#fff" stroke-width="2.5"/><path d="M14 20h20" stroke="#fff" stroke-width="2"/></svg>
    <h3>Premium Quality<br>Equipment</h3><p>Built to last. Engineered for<br>maximum performance.</p>
  </div>
  <div class="feature">
    <svg width="44" height="50" viewBox="0 0 44 48"><rect x="2" y="6" width="40" height="38" rx="3" fill="#1a4fd0"/><rect x="6" y="16" width="32" height="24" fill="#fff"/><text x="22" y="36" font-family="Oswald,sans-serif" font-size="18" fill="#1a4fd0" text-anchor="middle">24</text></svg>
    <h3>Same-Day Service<br>Available</h3><p>We're here when you<br>need us most.</p>
  </div>
  <div class="feature">
    <svg width="50" height="50" viewBox="0 0 48 48"><rect x="2" y="4" width="34" height="38" rx="3" fill="#1a4fd0"/><path d="M8 30h14M8 36h10" stroke="#fff" stroke-width="2.5"/><circle cx="36" cy="34" r="10" fill="#fff" stroke="#1a4fd0" stroke-width="3"/><path d="M36 29v9" stroke="#1a4fd0" stroke-width="3"/></svg>
    <h3>10-Year Warranty on<br>Select Products</h3><p>Long-lasting protection<br>you can trust.</p>
  </div>
  <div class="feature">
    <svg width="50" height="50" viewBox="0 0 48 48" fill="none" stroke="#1a4fd0" stroke-width="3"><circle cx="24" cy="14" r="9"/><path d="M6 34l10-8 8 6 8-6 10 8-10 10H16z" fill="#1a4fd0"/></svg>
    <h3>Local &amp; Trusted<br>Experts</h3><p>Proudly serving Florida<br>with reliable solutions.</p>
  </div>
</div>

<svg class="abs band" viewBox="0 0 1200 536" preserveAspectRatio="none" aria-hidden="true">
  <defs>
    <linearGradient id="bandFill" x1="0" y1="0" x2="0" y2="1"><stop offset="0" stop-color="#0b2d8f"/><stop offset=".6" stop-color="#0a2378"/><stop offset="1" stop-color="#0d3fb0"/></linearGradient>
  </defs>
  <path d="M0 0 C300 80 900 80 1200 0 V536 H0 Z" fill="#1a4fd0"/>
  <path d="M0 22 C300 102 900 102 1200 22 V520 C900 480 300 500 0 505 Z" fill="url(#bandFill)"/>
</svg>
<div class="abs band-house" role="img" aria-label="Modern two-storey house at dusk with water treatment units and water heaters lined up in front"></div>
<div class="abs badge">
  <svg style="position:absolute;left:28px;top:18px" width="52" height="58" viewBox="0 0 48 54"><path d="M24 2l20 8v16c0 14-9 22-20 26C13 48 4 40 4 26V10z" fill="#3d8cff" stroke="#bcd8ff" stroke-width="2"/><path d="M24 16v22M13 27h22" stroke="#fff" stroke-width="6"/></svg>
  <div class="badge-line">CLEANER WATER. SMARTER HOME.</div>
  <div class="badge-strong">GUARANTEED.</div>
</div>
<h2 class="abs head band-title">Whole-Home Solutions for<br><span>Cleaner, Healthier Living</span></h2>
<p class="abs band-text">From advanced water filtration to energy-efficient water heaters, we provide complete solutions tailored to your home and your needs.</p>
<div class="abs checks">
  <div class="check"><svg width="13" height="10" viewBox="0 0 14 10" fill="none" stroke="#fff" stroke-width="2"><path d="M1 5l4 4 8-8"/></svg>Better Water<br>Quality</div>
  <div class="check"><svg width="13" height="10" viewBox="0 0 14 10" fill="none" stroke="#fff" stroke-width="2"><path d="M1 5l4 4 8-8"/></svg>Energy<br>Savings</div>
  <div class="check"><svg width="13" height="10" viewBox="0 0 14 10" fill="none" stroke="#fff" stroke-width="2"><path d="M1 5l4 4 8-8"/></svg>Long-Lasting<br>Performance</div>
  <div class="check"><svg width="13" height="10" viewBox="0 0 14 10" fill="none" stroke="#fff" stroke-width="2"><path d="M1 5l4 4 8-8"/></svg>Protect Your<br>Home</div>
  <div class="check"><svg width="13" height="10" viewBox="0 0 14 10" fill="none" stroke="#fff" stroke-width="2"><path d="M1 5l4 4 8-8"/></svg>Safe for<br>You</div>
  <div class="check"><svg width="13" height="10" viewBox="0 0 14 10" fill="none" stroke="#fff" stroke-width="2"><path d="M1 5l4 4 8-8"/></svg>Eco-Friendly<br>Solutions</div>
</div>

<h2 class="abs head prod-title">All Products</h2>
<div class="btn" style="left:941px;top:1462px;width:127px;height:32px">View More Products</div>
<p class="abs prod-intro">High-quality water treatment products built for performance, efficiency and peace of mind.</p>
<div class="abs cards">
  <article class="card"><div class="card-photo" role="img" aria-label="Whole house water purification system"></div><h4 class="card-name">Water Purification System</h4><a class="card-link" href="#">Learn More ↗</a></article>
  <article class="card"><div class="card-photo" role="img" aria-label="Whole house water ionization system"></div><h4 class="card-name">Water Ionization System</h4><a class="card-link" href="#">Learn More ↗</a></article>
  <article class="card"><div class="card-photo" role="img" aria-label="Whole house water softener system"></div><h4 class="card-name">Water Softener System</h4><a class="card-link" href="#">Learn More ↗</a></article>
  <article class="card"><div class="card-photo" role="img" aria-label="Water heater sediment pre-filter"></div><h4 class="card-name">Heater Sediment Pre-Filter</h4><a class="card-link" href="#">Learn More ↗</a></article>
  <article class="card"><div class="card-photo" role="img" aria-label="Whole house UV water sterilization system"></div><h4 class="card-name">UV Water Sterilization</h4><a class="card-link" href="#">Learn More ↗</a></article>
  <article class="card"><div class="card-photo" role="img" aria-label="Ultimate whole house water treatment system"></div><h4 class="card-name">ULTIMATE Water Treatment</h4><a class="card-link" href="#">Learn More ↗</a></article>
  <article class="card"><div class="card-photo" role="img" aria-label="Under-sink reverse osmosis system with UV sterilizer"></div><h4 class="card-name">Under-Sink RO with UV</h4><a class="card-link" href="#">Learn More ↗</a></article>
  <article class="card"><div class="card-photo" role="img" aria-label="Smart water heater regulator"></div><h4 class="card-name">Smart Heater Regulator</h4><a class="card-link" href="#">Learn More ↗</a></article>
  <article class="card"><div class="card-photo" role="img" aria-label="Whole house water pressure booster"></div><h4 class="card-name">Water Pressure Booster</h4><a class="card-link" href="#">Learn More ↗</a></article>
  <article class="card"><div class="card-photo" role="img" aria-label="Hot water heater tank volume booster"></div><h4 class="card-name">Tank Volume Booster</h4><a class="card-link" href="#">Learn More ↗</a></article>
  <article class="card"><div class="card-photo" role="img" aria-label="Leak detector with automatic water shutoff valve"></div><h4 class="card-name">Leak Detector with Auto Shutoff</h4><a class="card-link" href="#">Learn More ↗</a></article>
  <article class="card"><div class="card-photo" role="img" aria-label="Whole house UV air purification system"></div><h4 class="card-name">UV Air Purification System</h4><a class="card-link" href="#">Learn More ↗</a></article>
  <article class="card"><div class="card-photo" role="img" aria-label="Leak detector alarm with mobile app"></div><h4 class="card-name">Leak Alarm with Mobile App</h4><a class="card-link" href="#">Learn More ↗</a></article>
  <article class="card"><div class="card-photo" role="img" aria-label="Multi-gas detector for carbon monoxide, gas and smoke"></div><h4 class="card-name">Multi-Gas Detector</h4><a class="card-link" href="#">Learn More ↗</a></article>
</div>

<section class="abs reviews">
  <h2 class="head reviews-title">What Our Customers Say</h2>
  <p class="reviews-sub">Real experiences from real customers who<br>trust Mr. Clear Brook.</p>
  <div class="quote" style="left:132px"><div class="quote-mark">“</div><p>Mr. Clear Brook has completely transformed the quality of water in our home. The products are reliable and the customer service is excellent!</p><div class="quote-author">Laura Whitfield</div></div>
  <div class="quote" style="left:448px"><div class="quote-mark">“</div><p>The water heater we purchased is highly efficient and has made a big difference in our energy bills. Highly recommend Mr. Clear Brook!</p><div class="quote-author">Daniel Ortega</div></div>
  <div class="quote" style="left:764px"><div class="quote-mark">“</div><p>Professional installation, great products, and peace of mind knowing my family has access to clean, safe water every day.</p><div class="quote-author">Grace Holloway</div></div>
</section>

<footer class="abs footer">
  <div class="brand" style="left:133px;top:70px;color:#fff"><i class="dot" style="background:#5aa6ff"></i>Mr. Clear Brook</div>
  <div class="brand" style="left:133px;top:100px;color:#fff"><i class="dot" style="background:#5aa6ff"></i>Mr. Hot Kettle</div>
  <p class="footer-about">Providing complete water &amp; home protection solutions with powerful products, trusted quality and professional service.</p>
  <div class="fcol" style="left:558px"><h5>Products</h5><ul><li>Whole House Filters</li><li>Water Filter Systems</li><li>Water Softeners</li><li>Water Heaters</li><li>Compact Water Softeners</li></ul></div>
  <div class="fcol" style="left:753px"><h5>Cquick Links</h5><ul><li>About Us</li><li>Installation</li><li>Reviews</li><li>Warranty</li><li>Blog</li></ul></div>
  <div class="fcol" style="left:882px"><h5>Contact Us</h5>
    <div class="ci"><svg width="12" height="12" viewBox="0 0 24 24" fill="#5aa6ff"><path d="M5 3h4l2 5-3 2a11 11 0 0 0 6 6l2-3 5 2v4a2 2 0 0 1-2 2A17 17 0 0 1 3 5a2 2 0 0 1 2-2z"/></svg>1300 555 017</div>
    <div class="ci"><svg width="12" height="12" viewBox="0 0 24 24" fill="none" stroke="#5aa6ff" stroke-width="2.5"><rect x="2" y="5" width="20" height="14"/><path d="M2 5l10 8 10-8"/></svg>info@mrclearbrook.example</div>
    <div class="ci"><svg width="12" height="14" viewBox="0 0 24 28" fill="#5aa6ff"><path d="M12 0a10 10 0 0 1 10 10c0 8-10 18-10 18S2 18 2 10A10 10 0 0 1 12 0z"/><circle cx="12" cy="10" r="4" fill="#0b1a5c"/></svg><span>Unit 4, 18 Harbor Lane, Fairview<br>NSW 2000, Australia</span></div>
    <div class="ci"><svg width="12" height="12" viewBox="0 0 24 24" fill="none" stroke="#5aa6ff" stroke-width="2.5"><circle cx="12" cy="12" r="10"/><path d="M12 6v6l4 3"/></svg><span>Mon - Fri: 8:30am - 5:00pm<br>Sat: 9:00am - 1:00pm</span></div>
  </div>
  <div class="footer-rule"></div>
  <div class="footer-copy">2025 Mr. Clear Brook &amp; Mr. Hot Kettle.<br>All Rights Reserved.</div>
</footer>

</body>
</html>
```